Lumora vale- referral cards for new customers

Hey,

I would like 1 set of business cards with the following details:

10% off any sales / coupon code
Our phone number: 4702938165
Menu :Lumoravale.example (for the menu)
A line left blank to hand write an activation code: either on top or just on one side

Include the Lumora Vale logo ( your choice of black or white logo)
This card is to drive orders for people to order a cannabis order with Lumora Vale. Please make the logo a large part of the card on both sides.

Target Market(s)

People who consume cannabis 21 and up

Industry/Entity Type

Business

Contact Information for Business Card

This business card will be given to customers so they can then give it to other customers and generate referalls. We need this card to be elegant, impressionable, professional, and something worth keeping and passing to friends.

Font styles to use
Decorative
Script

Colors
33a6d7
85acd3
3176b5
0455a3
0592cd
85cae6
cee9f5
eaf1f7
757575

Requirements
Must have
• Our website
• Phone Number
• The 10% off an order
• Spot for activation code
Nice to have
• Eye catching design
• Look classy
• Textured feel or textured look
Should not have
• Do not look super cannabis heady
• Do not look attractive to children

```html
<!DOCTYPE html>
<html lang="en">
<head>
<meta charset="utf-8">
<title>Lumora Vale – Referral Cards</title>
<link rel="stylesheet" href="https://fonts.googleapis.com/css2?family=Montserrat:wght@400;500;700&display=swap">
<style>
  :root {
    --page: #ffffff;
    --ink: #1c1c1c;
    --ink-soft: #3a3a3a;
    --grey: #757575;
    --blue: #3176b5;
    --blue-deep: #0455a3;
    --front-dark: #2a2a2a;
    --front-mid: #3d3d3d;
    --back-light: #f1f1f1;
    --back-mid: #dcdcdc;
    --mark: #5b6230;
    --mark-front: #b9d3d9;
  }
  * { box-sizing: border-box; margin: 0; padding: 0; }
  html, body {
    width: 1200px; height: 900px; overflow: hidden;
    background: var(--page);
    font-family: "Montserrat", sans-serif;
  }
  .canvas { position: relative; width: 1200px; height: 900px; }

  /* Standalone brand mark */
  .brand-lockup {
    position: absolute; left: 160px; top: 290px; width: 300px;
    display: flex; flex-direction: column; align-items: center;
  }
  .brand-lockup__circle {
    width: 200px; height: 200px; border-radius: 50%;
    background: var(--mark);
  }
  .brand-lockup__name {
    margin-top: 46px;
    font-size: 38px; font-weight: 500; letter-spacing: 2px;
    color: var(--ink);
  }

  /* Cards */
  .card {
    position: absolute; width: 377px; height: 377px;
    border-radius: 18px; overflow: hidden;
    box-shadow: 4px 6px 8px rgba(0,0,0,0.28);
  }
  .card__texture { position: absolute; inset: 0; }

  .card--front { left: 706px; top: 38px; }
  .card--front .card__texture {
    background: radial-gradient(circle at 50% 45%, var(--front-mid), var(--front-dark) 75%);
  }
  .card-front__mark {
    position: absolute; left: 0; right: 0; top: 70px;
    display: flex; flex-direction: column; align-items: center;
  }
  .card-front__circle {
    width: 170px; height: 170px; border-radius: 50%;
    background: var(--mark);
  }
  .card-front__name {
    margin-top: 22px;
    font-size: 30px; font-weight: 500; letter-spacing: 2px;
    color: var(--mark-front);
  }

  .card--back { left: 704px; top: 482px; }
  .card--back .card__texture {
    background: radial-gradient(circle at 40% 40%, var(--back-light), var(--back-mid) 90%);
  }
  .card-back__header {
    position: absolute; left: 14px; top: 24px;
    display: flex; align-items: center; gap: 12px;
  }
  .card-back__circle {
    width: 66px; height: 66px; border-radius: 50%;
    background: var(--mark); flex: none;
  }
  .card-back__name {
    font-size: 36px; font-weight: 500; letter-spacing: 1px;
    color: var(--grey); line-height: 1;
  }
  .card-back__menu {
    margin-top: 6px; font-size: 16px; color: var(--blue); white-space: nowrap;
  }
  .card-back__menu strong { font-weight: 700; margin-right: 8px; }

  .card-back__phone {
    position: absolute; left: 28px; top: 168px;
    font-size: 51px; font-weight: 500; color: var(--ink-soft);
    letter-spacing: 0.5px;
  }
  .card-back__offer {
    position: absolute; right: 22px; top: 280px;
    font-size: 25px; color: var(--blue);
  }
  .card-back__offer strong { font-weight: 700; }
  .card-back__code {
    position: absolute; left: 121px; width: 230px; top: 346px;
    border-top: 1px solid var(--blue);
    text-align: center; font-size: 12px; color: var(--blue-deep);
    padding-top: 1px;
  }
</style>
</head>
<body>
<main class="canvas">

  <section class="brand-lockup">
    <div class="brand-lockup__circle"></div>
    <div class="brand-lockup__name">Lumora Vale</div>
  </section>

  <article class="card card--front">
    <div class="card__texture" role="img" aria-label="Dark grey macro leaf-vein texture background"></div>
    <div class="card-front__mark">
      <div class="card-front__circle"></div>
      <div class="card-front__name">Lumora Vale</div>
    </div>
  </article>

  <article class="card card--back">
    <div class="card__texture" role="img" aria-label="Light grey macro leaf-vein texture background"></div>
    <header class="card-back__header">
      <div class="card-back__circle"></div>
      <div>
        <div class="card-back__name">Lumora Vale</div>
        <div class="card-back__menu"><strong>Menu :</strong>Lumoravale.example</div>
      </div>
    </header>
    <div class="card-back__phone">4702938165</div>
    <div class="card-back__offer"><strong>10% off</strong> any sales</div>
    <div class="card-back__code">coupon code</div>
  </article>

</main>
</body>
</html>
```